Idea for facelift on local Hong Kong family business website to get ready for International business

We are a family business in Hong Kong doing high quality aluminium and fibre glass ladder systems. We are currently exploring International markets and are looking for ideas for web site design facelift.

Because we want to attract good talents, we are not asking the designer to finish the work. The best idea wins, even if unfinished.

It is however most important that sample HTML / CSS code is done to show that the designer knows responsive web, and that it is feasible, not just looks good.

Depending on the outcome, we will put out additional tasks for further materialising of the design and for full coding of the web site

This is the current web-site for the ladder brand we will be promoting overseas:

https://www.vr-holdfast.com

This is the parent company, which does business in Hong Kong (for reference only, subsequent additional facelift tasks will come after we have finished the product site.

http://www.lumwahltd.com.hk

Remember, do just enough to show us you really know responsive web design including coding. It is ok use templates. We are looking for good idea from good designer who also knows HTML and CSS. For this project we are looking for quality, not quantity.

Target Market(s)

International customers

Industry/Entity Type

Hardware / Ladder Systems

Coding

Coded - Design and coding required

Number of Pages Required

3 page

Requirements
Must have
• Enough HTML CSS and optionally JS to show designer knows responsive web design coding

```html
<!DOCTYPE html>
<html lang="en">
<head>
<meta charset="utf-8">
<title>VR Holdfast – Ladders Specialist</title>
<link href="https://fonts.googleapis.com/css2?family=Poppins:wght@500;600;700&family=Roboto:wght@300;400&display=swap" rel="stylesheet">
<style>
:root{
  --red:#d3202a;
  --red-dark:#b8232b;
  --lime:#8cc63f;
  --sky:#6cc4ee;
  --orange:#ea5a2c;
  --ink:#1d1d1f;
  --text:#444;
  --page:#ffffff;
  --mist:#ececec;
}
*{box-sizing:border-box;margin:0;padding:0}
html,body{width:1200px;height:2429px;overflow:hidden;background:var(--page)}
body{position:relative;font-family:"Roboto",sans-serif;color:var(--text)}
.site{position:absolute;left:690px;top:123px;width:268px;height:2306px;background:var(--page)}
.site-header{position:absolute;top:0;left:0;width:100%;height:54px;background:var(--page);z-index:3}
.brand{position:absolute;left:50%;top:6px;transform:translateX(-50%);width:76px;height:76px;border-radius:50%;background:#fff;border:2px solid var(--mist);display:flex;align-items:center;justify-content:center;text-align:center;font-family:"Poppins",sans-serif;font-weight:700;font-size:10px;line-height:1.1;color:var(--red);box-shadow:0 2px 6px rgba(0,0,0,.15)}
.menu-toggle{position:absolute;right:10px;top:15px;width:34px;height:24px}
.hero{position:absolute;top:54px;left:0;width:100%;height:400px;overflow:hidden}
.hero-photo{position:absolute;inset:0;height:280px;background:linear-gradient(160deg,#9aa59a 0%,#7b8d5f 35%,#5f6e4a 60%,#8a8f86 100%)}
.hero-photo::after{content:"";position:absolute;inset:0;background:rgba(40,40,40,.35)}
.hero-curve{position:absolute;left:0;top:240px;width:100%;height:160px}
.hero-copy{position:absolute;top:80px;left:0;width:100%;text-align:center;color:#fff;z-index:2}
.hero-title{font-family:"Poppins",sans-serif;font-weight:600;font-size:24px;line-height:1.2}
.hero-tag{font-family:"Poppins",sans-serif;font-weight:500;font-size:12px;color:var(--lime);margin-top:10px}
.hero-text{font-size:10.5px;line-height:1.6;margin:12px 12px 0;font-weight:400}
.btn-solid{display:inline-block;margin-top:10px;background:var(--red-dark);color:#fff;font-family:"Poppins",sans-serif;font-weight:500;font-size:12px;padding:9px 32px}
.lines{position:absolute;top:300px;left:0;width:100%;height:100px;z-index:2}
.line{position:absolute;font-family:"Poppins",sans-serif;font-weight:600;font-size:15px;color:var(--ink);white-space:nowrap}
.line::before{content:"";position:absolute;left:-15px;top:-5px;width:32px;height:32px;border-radius:50%;z-index:-1}
.line-down{left:24px;top:6px}.line-down::before{background:var(--lime)}
.line-home{left:167px;top:5px}.line-home::before{background:var(--sky)}
.line-up{left:110px;top:49px}.line-up::before{background:var(--orange)}
.range{position:absolute;top:454px;left:0;width:100%;height:102px;text-align:center}
.range-title{font-family:"Poppins",sans-serif;font-weight:600;font-size:16px;color:var(--ink);margin-top:20px}
.range-arrow{margin-top:10px}
.products{position:absolute;top:558px;left:0;width:100%}
.product{position:relative;height:227px;margin-bottom:9px;overflow:hidden}
.product-bg{position:absolute;inset:0;background:linear-gradient(180deg,#e8e8e8,#d2d2d2)}
.product-card{position:absolute;left:8px;right:8px;top:16px;bottom:14px;background:rgba(255,255,255,.92);text-align:center;padding-top:44px}
.mascot{position:absolute;left:50%;top:-14px;transform:translateX(-50%);width:50px;height:48px;border-radius:50%;background:radial-gradient(circle at 50% 35%,#f3c318 0 30%,#e56a2a 31% 100%)}
.product-name{font-family:"Poppins",sans-serif;font-weight:700;font-size:10px;line-height:14px;color:var(--red);letter-spacing:.5px}
.product-text{font-size:11.5px;line-height:1.7;color:var(--text);margin:6px 20px 0;font-weight:400;text-align:left}
.btn-outline{display:inline-block;margin-top:9px;border:2px solid var(--red);color:var(--red);font-size:11px;padding:7px 0;width:118px;border-radius:2px;background:#fff}
.tone-ladder .product-bg{background:linear-gradient(180deg,#f1eef3,#ddd3e3)}
.tone-logistic .product-bg{background:linear-gradient(180deg,#e9ece0,#d9d9d9)}
.tone-scaffold .product-bg{background:linear-gradient(180deg,#d6d6d6,#ececec)}
.tone-contact .product-bg{background:linear-gradient(90deg,#cfcfcf,#f5f5f5 50%,#cfcfcf)}
.tone-contact .product-card{background:transparent}
.site-footer{position:absolute;top:2037px;left:0;width:100%;height:269px;background:linear-gradient(180deg,#cfcfcf,#b9b9b9 60%,#d8d8d8)}
.footer-curve{position:absolute;top:0;left:0;width:100%;height:40px}
.footer-brand{top:8px;width:70px;height:70px}
.social{position:absolute;top:98px;left:0;width:100%;display:flex;justify-content:center;gap:18px}
.social span{width:26px;height:26px;border-radius:50%;border:3px solid var(--red);background:#fff}
.contact{position:absolute;top:148px;left:0;width:100%;font-size:11.5px;color:#222}
.contact-row{display:flex;align-items:flex-start;justify-content:center;gap:8px;margin-bottom:12px;line-height:1.45}
.copyright{position:absolute;bottom:6px;left:0;width:100%;text-align:center;font-size:10px;color:#333}
</style>
</head>
<body>
<main class="site">
  <header class="site-header">
    <div class="brand">VR<br>HOLDFAST</div>
    <svg class="menu-toggle" viewBox="0 0 34 24" aria-label="Menu"><g stroke="#d3202a" stroke-width="3" stroke-linecap="round"><line x1="4" y1="3" x2="32" y2="3"/><line x1="12" y1="12" x2="32" y2="12"/><line x1="18" y1="21" x2="32" y2="21"/></g></svg>
  </header>

  <section class="hero">
    <div class="hero-photo" role="img" aria-label="Worker in red helmet and hi-vis vest climbing at height"></div>
    <svg class="hero-curve" viewBox="0 0 268 160" preserveAspectRatio="none"><defs><linearGradient id="steel" x1="0" y1="0" x2="0" y2="1"><stop offset="0" stop-color="#fafafa"/><stop offset="1" stop-color="#c8c8c8"/></linearGradient></defs><path d="M0 32 Q134 -10 268 32 L268 160 L0 160Z" fill="url(#steel)"/></svg>
    <div class="hero-copy">
      <h1 class="hero-title">Ladders Specialist</h1>
      <p class="hero-tag">Work at Height Safety Tools Equipment</p>
      <p class="hero-text">Our mission is to make sure you work safely no matter at work or at home to prevent any injury especially in the construction industry.</p>
      <span class="btn-solid">SHOP NOW</span>
    </div>
    <div class="lines">
      <span class="line line-down">Step-Down</span>
      <span class="line line-home">Step-Home</span>
      <span class="line line-up">Step-Up</span>
    </div>
  </section>

  <section class="range">
    <h2 class="range-title">VR HOLDFAST Products include</h2>
    <svg class="range-arrow" width="32" height="32" viewBox="0 0 32 32" aria-hidden="true"><circle cx="16" cy="16" r="14" fill="none" stroke="#d3202a" stroke-width="2"/><path d="M16 8v15M10 17l6 6 6-6" fill="none" stroke="#d3202a" stroke-width="2" stroke-linecap="round"/></svg>
  </section>

  <section class="products">
    <article class="product tone-ladder">
      <div class="product-bg" role="img" aria-label="Aluminium ladder photo"></div>
      <div class="product-card">
        <div class="mascot" role="img" aria-label="Brand mascot carrying a ladder"></div>
        <p class="product-name">VR LADDER</p>
        <p class="product-text">“VR LADDER” ladders are made of both Aluminium and Fiberglass which are suitable for industry, business, shops, schools, home and garden. [...]</p>
        <span class="btn-outline">SHOP NOW</span>
      </div>
    </article>
    <article class="product tone-logistic">
      <div class="product-bg" role="img" aria-label="Roll container photo"></div>
      <div class="product-card">
        <div class="mascot" role="img" aria-label="Brand mascot with a crate"></div>
        <p class="product-name">VR LOGISTIC</p>
        <p class="product-text">VR LOGISTIC provides all kinds of facilities to save your energy for transporting heavy goods Safely. Our items include roll containers, [...]</p>
        <span class="btn-outline">SHOP NOW</span>
      </div>
    </article>
    <article class="product">
      <div class="product-bg" role="img" aria-label="Platform ladder on castors photo"></div>
      <div class="product-card">
        <div class="mascot" role="img" aria-label="Brand mascot with a wheel"></div>
        <p class="product-name">VR CASTOR</p>
        <p class="product-text">Wheel and Castor. VR CASTOR is to develop the best wheel, the best castor for all of our customer’s requirements. Functionality, efficiency, [...]</p>
        <span class="btn-outline">SHOP NOW</span>
      </div>
    </article>
    <article class="product tone-scaffold">
      <div class="product-bg" role="img" aria-label="Scaffold tower photo"></div>
      <div class="product-card">
        <div class="mascot" role="img" aria-label="Brand mascot with scaffold frame"></div>
        <p class="product-name">VR SCAFFOLD</p>
        <p class="product-text">Scaffolding requires Safety, Flexible combination, Easy assembling but strong at the same time. VR SCAFFOLD ensures its maximum stability and Safe to use [...]</p>
        <span class="btn-outline">SHOP NOW</span>
      </div>
    </article>
    <article class="product">
      <div class="product-bg" role="img" aria-label="Safety helmet and harness photo"></div>
      <div class="product-card">
        <div class="mascot" role="img" aria-label="Brand mascot with tools"></div>
        <p class="product-name">VR TOOLS</p>
        <p class="product-text">VR TOOLS provides all kinds of Safety Equipments including insulated screwdrivers, multi-function gloves, shoes, helmet, harness, torch and more</p>
        <span class="btn-outline">SHOP NOW</span>
      </div>
    </article>
    <article class="product tone-contact">
      <div class="product-bg" role="img" aria-label="Technical drawing of work platforms"></div>
      <div class="product-card">
        <div class="mascot" role="img" aria-label="Brand mascot waving"></div>
        <p class="product-name">VR HOLDFAST</p>
        <p class="product-text">Good design is important in working at height. Cannot find suitable item in the market ? Please write to us, we can make it for you exclusively.</p>
        <span class="btn-outline">CONTACT US</span>
      </div>
    </article>
  </section>

  <footer class="site-footer">
    <svg class="footer-curve" viewBox="0 0 268 40" preserveAspectRatio="none"><path d="M0 0 L268 0 L268 2 Q134 70 0 2Z" fill="#fff"/></svg>
    <div class="brand footer-brand">VR<br>HOLDFAST</div>
    <nav class="social" aria-label="Social links"><span aria-label="Video channel"></span><span aria-label="Microblog"></span><span aria-label="Social network"></span><span aria-label="Photo sharing"></span><span aria-label="Pin boards"></span></nav>
    <div class="contact">
      <p class="contact-row"><svg width="16" height="16" viewBox="0 0 24 24"><path d="M6.6 10.8a15 15 0 0 0 6.6 6.6l2.2-2.2a1 1 0 0 1 1-.25 11 11 0 0 0 3.6.6 1 1 0 0 1 1 1V20a1 1 0 0 1-1 1A17 17 0 0 1 3 4a1 1 0 0 1 1-1h3.5a1 1 0 0 1 1 1 11 11 0 0 0 .6 3.6 1 1 0 0 1-.25 1z" fill="#d3202a"/></svg>+852 2555 0187</p>
      <p class="contact-row"><svg width="16" height="14" viewBox="0 0 24 18"><rect width="24" height="18" rx="2" fill="#d3202a"/><path d="M1 2l11 8 11-8" fill="none" stroke="#fff" stroke-width="2"/></svg>info@vr-holdfast.com</p>
      <p class="contact-row"><svg width="14" height="18" viewBox="0 0 14 20"><path d="M7 0a7 7 0 0 0-7 7c0 5 7 13 7 13s7-8 7-13a7 7 0 0 0-7-7z" fill="#d3202a"/><circle cx="7" cy="7" r="2.6" fill="#fff"/></svg><span>Lorem ipsum dolor sit<br>amet, consectetue</span></p>
    </div>
    <p class="copyright">©Copyright 2020 VR HOLDFAST All rights reserved.</p>
  </footer>
</main>
</body>
</html>
```